Plume Vert Harvest

Need website design for a new company (Trademark: Plume Vert Harvest). It's:<br/>-- Organic<br/>-- Raw<br/>-- Plant-based food<br/>-- Kosher<br/> Vegetarian and fruits) concept. Packaging with be completely sustainable. It will essentially be "The Best Food On The Planet." <br/><br/>More info:<br/>a) Main ingredients would be salad, raw zucchini fettuccini noodles, and more plant-based prepared foods; <br/>b) Sauces or dressings to go with the a) above (small portions); <br/>c) Toppings/garnishes; <br/>d) Juices in bottles. <br/><br/>See logos attached. Please design pages for photos of the products which will be packaged for sale (not yet provided). You will notices that there is one logo--the one in color--where the accent is incorrect. We would probably like to use this because it's in color but we need the proper accent above the "e".<br/><br/>We like unusual designs.<br/><br/>Please create in WordPress.<br/><br/>Please send any questions. Thank you for participating.

```html
<!DOCTYPE html>
<html lang="en">
<head>
<meta charset="utf-8">
<title>Plume Vert Harvest</title>
<link rel="stylesheet" href="https://fonts.googleapis.com/css2?family=Bebas+Neue&family=Poppins:wght@300;400;500;600&family=Vollkorn:ital,wght@1,400;1,500&display=swap">
<style>
:root{
  --green-dark:#1d5e3a;
  --green-deep:#174f30;
  --green-btn:#2f9a45;
  --green-btn-dark:#1f7a35;
  --green-light:#5cbf5e;
  --text:#333;
  --muted:#888;
  --line:#e6e6e6;
  --white:#fff;
  --grey-bg:#f2f2f2;
}
*{box-sizing:border-box;margin:0;padding:0}
html,body{width:1200px;height:5120px;overflow:hidden}
body{position:relative;font-family:"Poppins",sans-serif;color:var(--text);background:var(--white)}
.abs{position:absolute}
.serif{font-family:"Vollkorn",serif;font-style:italic;font-weight:400}
.center{text-align:center}
.para{font-size:14px;line-height:27px;color:var(--muted);font-weight:300}
.btn{position:absolute;display:flex;align-items:center;justify-content:center;background:linear-gradient(90deg,var(--green-btn),var(--green-btn-dark));color:#fff;font-family:"Vollkorn",serif;font-style:italic;font-size:18px;border-radius:3px}
.photo{position:absolute}

/* top bar */
.topbar{top:0;left:0;width:1200px;height:40px;background:var(--green-dark)}
.social-dot{position:absolute;width:26px;height:26px;border-radius:50%;top:7px}
.topbar .phone{position:absolute;right:76px;top:0;height:40px;display:flex;align-items:center;gap:8px;color:#fff;font-size:15px}
/* nav */
.nav{top:40px;left:0;width:1200px;height:100px;background:#fff}
.nav a{position:absolute;top:42px;font-size:15px;color:#333;text-decoration:none;transform:translateX(-50%)}
.nav a.active{color:var(--green-btn)}
.nav a.active::after{content:"";position:absolute;left:0;bottom:-8px;width:22px;height:2px;background:var(--green-btn)}
.brand{position:absolute;left:510px;top:3px;width:180px;height:180px;border-radius:50%;background:#fff;z-index:5;display:flex;align-items:center;justify-content:center;text-align:center;font-family:"Vollkorn",serif;font-style:italic;font-size:28px;line-height:32px;color:var(--green-dark);box-shadow:0 2px 6px rgba(0,0,0,.08)}
/* hero */
.hero{top:140px;left:0;width:1200px;height:536px;background:radial-gradient(ellipse at 50% 45%,#2c3f52,#17232e 70%),#1a2630}
.hero-greens{top:560px;left:0;width:1200px;height:116px;background:linear-gradient(180deg,rgba(40,90,40,0),#2f6a2c 70%)}
.hero h1{position:absolute;top:228px;left:0;width:1200px;text-align:center;font-family:"Bebas Neue",sans-serif;font-weight:400;font-size:66px;color:#fff;letter-spacing:.5px}
/* why */
.section-title{font-size:46px;color:var(--green-dark)}
.feature{position:absolute;width:200px;text-align:center;top:892px}
.feature .ring{width:104px;height:104px;margin:0 auto;border-radius:50%;border:2px solid var(--green-dark);display:flex;align-items:center;justify-content:center}
.feature .ring-inner{width:92px;height:92px;border-radius:50%;border:1px solid var(--green-dark);display:flex;align-items:center;justify-content:center}
.feature p{margin-top:22px;font-size:18px;color:#333}
/* split panels */
.panel{position:absolute;left:730px;width:470px;background:var(--green-dark);color:#fff;text-align:center}
.panel h2{font-family:"Vollkorn",serif;font-style:italic;font-weight:400;font-size:36px}
.panel .para{color:#e5efe8}
.dot{position:absolute;width:14px;height:14px;border-radius:50%;border:2px solid #fff}
.dot.on{background:#fff}
/* provide */
.provide{top:2932px;left:0;width:1200px;height:626px;background:linear-gradient(135deg,#1f6640,#174f30)}
.card{position:absolute;top:3142px;width:245px;height:348px;background:#fff;text-align:center}
.card .shot{position:absolute;left:36px;top:28px;width:173px;height:200px}
.card h3{position:absolute;top:262px;width:100%;font-size:16px;font-weight:600;color:#222}
.card .price{position:absolute;top:292px;width:100%;font-size:16px;color:#222}
.card.featured{background:var(--green-light)}
.card.featured h3,.card.featured .price{color:#8fd28f}
/* testimonials */
.tcard{position:absolute;top:3727px;width:322px;height:324px;background:#fff;box-shadow:0 0 14px rgba(0,0,0,.07)}
.tcard .avatar{position:absolute;left:26px;top:28px;width:66px;height:66px;border-radius:50%}
.tcard .name{position:absolute;left:106px;top:40px;font-size:16px;font-weight:600;color:#222}
.tcard .role{position:absolute;left:106px;top:66px;font-size:13px;color:var(--green-btn)}
.tcard .rule{position:absolute;left:0;top:112px;width:100%;height:1px;background:var(--line)}
.tcard .quote{position:absolute;left:28px;top:134px;width:272px;font-size:13.5px;line-height:27px;color:var(--muted);font-weight:300}
.tcard .mark{position:absolute;right:24px;bottom:20px}
.arrow{position:absolute;top:3874px;width:48px;height:48px;border-radius:50%;background:#fff;border:1px solid #ddd;display:flex;align-items:center;justify-content:center}
/* videos */
.videos{top:4150px;left:0;width:1200px;height:586px;background:var(--grey-bg)}
.thumb{position:absolute;top:4293px;width:322px;height:205px}
.play{position:absolute;left:136px;top:82px;width:50px;height:36px;border-radius:8px;background:#e3221c;display:flex;align-items:center;justify-content:center}
.vcap{position:absolute;width:322px;text-align:center}
.vcap h4{font-size:16px;font-weight:600;line-height:26px;color:#222;text-transform:uppercase}
.vcap .para{margin-top:18px}
/* footer */
.footer{top:4736px;left:0;width:1200px;height:384px;background:var(--green-dark);color:#d9e8de}
.footer h5{position:absolute;top:50px;font-size:15px;font-weight:600;color:#fff;letter-spacing:.5px}
.footer .ftext{position:absolute;font-size:13.5px;line-height:27px;font-weight:300}
.footer .links a{position:absolute;left:803px;font-size:13.5px;color:#d9e8de;text-decoration:none}
.fsocial{position:absolute;top:4985px;width:40px;height:40px;border-radius:50%;border:1.5px solid #fff}
.copyright{position:absolute;top:5078px;left:0;width:1200px;height:42px;border-top:1px solid rgba(255,255,255,.15);text-align:center;line-height:42px;font-size:13px;color:#d9e8de}
</style>
</head>
<body>

<!-- Top bar -->
<div class="abs topbar">
  <span class="social-dot" style="left:80px;background:var(--green-btn)"></span>
  <span class="social-dot" style="left:116px;background:#fff;opacity:.25"></span>
  <span class="social-dot" style="left:152px;background:#fff;opacity:.25"></span>
  <span class="social-dot" style="left:188px;background:#fff;opacity:.25"></span>
  <div class="phone">
    <svg width="24" height="24" viewBox="0 0 24 24"><circle cx="12" cy="12" r="12" fill="#2f9a45"/><path d="M8.5 6.5l2 2-1.2 1.6c.8 1.6 2 2.8 3.6 3.6l1.6-1.2 2 2-1.4 1.8c-3.8-.6-7.2-4-7.8-7.8z" fill="#fff"/></svg>
    123 456 7890
  </div>
</div>

<!-- Navigation -->
<nav class="abs nav">
  <a class="active" href="#" style="left:262px">Home</a>
  <a href="#" style="left:356px">Products</a>
  <a href="#" style="left:453px">Videos</a>
  <a href="#" style="left:759px">About Us</a>
  <a href="#" style="left:880px">How To Order</a>
  <a href="#" style="left:1000px">Contact</a>
  <div class="brand">Plume Vert<br>Harvest</div>
</nav>

<!-- Hero -->
<section class="abs hero" role="img" aria-label="Top view of fresh vegetables, onions, garlic, tomatoes and spices on a dark wooden table">
  <h1>THE BEST FOOD ON THE PLANET</h1>
</section>
<div class="abs hero-greens" role="img" aria-label="Fresh herbs along the bottom edge"></div>

<!-- Why choose us -->
<h2 class="abs serif section-title center" style="top:734px;left:0;width:1200px">Why Choose Us ?</h2>
<p class="abs para center" style="top:798px;left:300px;width:600px">Lorem Ipsum is simply dummy text of the printing and typesetting industry. Lorem Ipsum has been the industry's standard</p>

<div class="feature" style="left:120px">
  <div class="ring"><div class="ring-inner">
    <svg width="48" height="40" viewBox="0 0 48 40" fill="none" stroke="#1d5e3a" stroke-width="2"><path d="M4 36c8-4 14-10 16-20C12 14 6 22 4 36z"/><path d="M20 30c8 0 20-6 24-24-14 2-22 10-24 24z"/></svg>
  </div></div>
  <p>Organic</p>
</div>
<div class="feature" style="left:375px">
  <div class="ring"><div class="ring-inner">
    <svg width="40" height="40" viewBox="0 0 40 40" fill="none" stroke="#1d5e3a" stroke-width="2"><ellipse cx="20" cy="24" rx="13" ry="12"/><path d="M20 12c0-4 2-7 5-8"/><path d="M12 30l14-12"/></svg>
  </div></div>
  <p>Raw</p>
</div>
<div class="feature" style="left:624px">
  <div class="ring"><div class="ring-inner">
    <svg width="40" height="44" viewBox="0 0 40 44" fill="none" stroke="#1d5e3a" stroke-width="2"><path d="M20 14c-4-3-14-3-14 10 0 10 7 17 11 17 2 0 2-1 3-1s1 1 3 1c4 0 11-7 11-17 0-13-10-13-14-10z"/><path d="M20 14c0-5 2-9 5-11"/><path d="M21 9c3-3 7-3 9-2-2 3-6 4-9 2z"/></svg>
  </div></div>
  <p>Plant-Based</p>
</div>
<div class="feature" style="left:874px">
  <div class="ring"><div class="ring-inner">
    <svg width="46" height="46" viewBox="0 0 46 46" fill="none" stroke="#1d5e3a" stroke-width="2"><path d="M23 4l17 29H6z"/><path d="M23 42L6 13h34z"/></svg>
  </div></div>
  <p>Kosher</p>
</div>

<!-- Thai noodles -->
<div class="photo" style="top:1100px;left:0;width:730px;height:446px;background:linear-gradient(135deg,#c9b58a,#8a6a3c 45%,#5b7a3a)" role="img" aria-label="Close-up of Thai noodles with shredded carrot, cabbage and herbs"></div>
<div class="panel" style="top:1100px;height:446px">
  <h2 style="margin-top:96px">Thai Noodles</h2>
  <p class="para" style="margin:12px auto 0;width:320px">Lorem Ipsum is simply dummy text of the print and the typesetting industry. Lorem Ipsum has been the industry's standard.</p>
</div>
<div class="btn" style="top:1343px;left:886px;width:161px;height:52px;background:linear-gradient(90deg,#3aa84f,#2c8f42)">SHOP NOW</div>
<span class="dot on" style="top:1438px;left:907px"></span>
<span class="dot" style="top:1438px;left:939px"></span>
<span class="dot" style="top:1438px;left:971px"></span>
<span class="dot" style="top:1438px;left:1003px"></span>

<!-- Product 2 -->
<div class="abs" style="top:1650px;left:221px;width:440px;height:292px;border:2px solid var(--green-dark)"></div>
<h2 class="abs serif" style="top:1680px;left:288px;font-size:36px;color:var(--green-dark)">Product 2</h2>
<p class="abs para" style="top:1742px;left:278px;width:320px">Lorem Ipsum is simply dummy text of the print and the typesetting industry. Lorem Ipsum has been the industry's standard.</p>
<div class="btn" style="top:1844px;left:286px;width:161px;height:50px">SHOP NOW</div>
<div class="photo" style="top:1590px;left:600px;width:374px;height:388px;border-radius:45% 40% 45% 40%;background:radial-gradient(circle at 45% 50%,#e0762a,#4f8a2c 55%,rgba(255,255,255,0) 72%)" role="img" aria-label="Assorted fresh vegetables and berries: lettuce, pepper, carrot, tomato, zucchini, cherries"></div>

<!-- Product 3 -->
<div class="photo" style="top:2017px;left:0;width:730px;height:448px;background:linear-gradient(120deg,#2f4e6e,#b99b5a 50%,#5d7a3d)" role="img" aria-label="Person in an apron tossing a green salad in a wooden bowl on a kitchen counter"></div>
<div class="panel" style="top:2017px;height:448px"></div>
<div class="photo" style="top:2061px;left:930px;width:80px;height:125px;border-radius:6px;background:linear-gradient(160deg,#8fbf5a,#4c7d2e)" role="img" aria-label="Packaged salad bag"></div>
<h2 class="abs serif center" style="top:2196px;left:730px;width:470px;font-size:36px;color:#fff">Product 3</h2>
<p class="abs para center" style="top:2254px;left:805px;width:320px;color:#e5efe8">Lorem Ipsum is simply dummy text of the print and the typesetting industry. Lorem Ipsum has been the industry's standard.</p>
<div class="btn" style="top:2355px;left:886px;width:161px;height:50px;background:linear-gradient(90deg,#3aa84f,#2c8f42)">SHOP NOW</div>

<!-- Raw zucchini -->
<h2 class="abs serif" style="top:2578px;left:234px;width:420px;font-size:36px;line-height:42px;color:var(--green-dark)">Raw Zucchini Fettuccini Noodles</h2>
<p class="abs para" style="top:2666px;left:236px;width:320px">Lorem Ipsum is simply dummy text of the print and the typesetting industry. Lorem Ipsum has been the industry's standard.</p>
<div class="btn" style="top:2763px;left:236px;width:162px;height:50px">SHOP NOW</div>
<div class="photo" style="top:2528px;left:705px;width:338px;height:344px;border-radius:18px;background:linear-gradient(135deg,#e7ece8,#8cb26a 50%,#dfe5df)" role="img" aria-label="Clear tray of zucchini spiral noodles with a product label"></div>

<!-- We provide our best -->
<section class="abs provide" role="img" aria-label="Dark green leafy background"></section>
<h2 class="abs serif center" style="top:2988px;left:0;width:1200px;font-size:46px;color:#fff">We Provide Our Best</h2>
<p class="abs para center" style="top:3052px;left:300px;width:600px;color:#d8e8dd">Lorem Ipsum is simply dummy text of the printing and typesetting industry. Lorem Ipsum has been the industry's standard</p>

<div class="card" style="left:78px">
  <div class="shot" style="background:linear-gradient(135deg,#dfe5df,#9cc06a)" role="img" aria-label="Tray of zucchini noodles"></div>
  <h3>PRODUCT NAME</h3><p class="price">$32.00</p>
</div>
<div class="card featured" style="left:344px">
  <div class="shot" style="left:92px;width:62px;background:#4d9e48;border-radius:14px" role="img" aria-label="Bottle silhouette"></div>
  <svg class="abs" style="left:96px;top:118px" width="54" height="54" viewBox="0 0 54 54" stroke="#bfe6bf" stroke-width="1.5"><path d="M27 0v54M0 27h54"/></svg>
  <h3>PRODUCT NAME</h3><p class="price">$32.00</p>
</div>
<div class="card" style="left:608px">
  <div class="shot" style="left:66px;width:113px;background:linear-gradient(160deg,#9bcb5c,#4c8a2e);border-radius:6px" role="img" aria-label="Packaged salad bag"></div>
  <h3>PRODUCT NAME</h3><p class="price">$32.00</p>
</div>
<div class="card" style="left:875px">
  <div class="shot" style="left:94px;width:58px;background:linear-gradient(180deg,#d9efd0 0 14%,#3da33d 14%);border-radius:12px" role="img" aria-label="Bottle of green juice"></div>
  <h3>PRODUCT NAME</h3><p class="price">$32.00</p>
</div>

<!-- Testimonials -->
<h2 class="abs center" style="top:3636px;left:0;width:1200px;font-size:44px;font-weight:400;color:var(--green-dark)">Client Testimonials</h2>

<div class="arrow" style="left:16px"><svg width="22" height="14" viewBox="0 0 22 14" fill="none" stroke="#666" stroke-width="1.5"><path d="M21 7H2M8 1L2 7l6 6"/></svg></div>
<div class="arrow" style="left:1137px"><svg width="22" height="14" viewBox="0 0 22 14" fill="none" stroke="#666" stroke-width="1.5"><path d="M1 7h19M14 1l6 6-6 6"/></svg></div>

<div class="tcard" style="left:78px">
  <div class="avatar" style="background:#c9b8a6" role="img" aria-label="Client portrait"></div>
  <p class="name">CLIENT NAME</p><p class="role">Lorem Ipsum is dummy text</p>
  <div class="rule"></div>
  <p class="quote">Lorem Ipsum is simply dummy text of the printing and typesetting industry. Lorem Ipsum has been the industry's standard dummy text ever since the 1500s, when an unknown printer took.</p>
  <svg class="mark" width="42" height="34" viewBox="0 0 42 34" fill="#c7ecc0"><path d="M2 2h16v16c0 8-5 13-14 14v-6c4-1 6-3 6-8H2zM24 2h16v16c0 8-5 13-14 14v-6c4-1 6-3 6-8h-8z"/></svg>
</div>
<div class="tcard" style="left:439px">
  <div class="avatar" style="background:#cdb08e" role="img" aria-label="Client portrait"></div>
  <p class="name">CLIENT NAME</p><p class="role">Lorem Ipsum is dummy text</p>
  <div class="rule"></div>
  <p class="quote">Lorem Ipsum is simply dummy text of the printing and typesetting industry. Lorem Ipsum has been the industry's standard dummy text ever since the 1500s, when an unknown printer took.</p>
  <svg class="mark" width="42" height="34" viewBox="0 0 42 34" fill="#c7ecc0"><path d="M2 2h16v16c0 8-5 13-14 14v-6c4-1 6-3 6-8H2zM24 2h16v16c0 8-5 13-14 14v-6c4-1 6-3 6-8h-8z"/></svg>
</div>
<div class="tcard" style="left:799px">
  <div class="avatar" style="background:#6b5a4e" role="img" aria-label="Client portrait"></div>
  <p class="name">CLIENT NAME</p><p class="role">Lorem Ipsum is dummy text</p>
  <div class="rule"></div>
  <p class="quote">Lorem Ipsum is simply dummy text of the printing and typesetting industry. Lorem Ipsum has been the industry's standard dummy text ever since the 1500s, when an unknown printer took.</p>
  <svg class="mark" width="42" height="34" viewBox="0 0 42 34" fill="#c7ecc0"><path d="M2 2h16v16c0 8-5 13-14 14v-6c4-1 6-3 6-8H2zM24 2h16v16c0 8-5 13-14 14v-6c4-1 6-3 6-8h-8z"/></svg>
</div>

<!-- Videos -->
<section class="abs videos"></section>
<h2 class="abs center" style="top:4212px;left:0;width:1200px;font-size:44px;font-weight:400;color:var(--green-dark)">Our Videos</h2>
<div class="thumb" style="left:258px;background:linear-gradient(180deg,#b7bdb0 0 30%,#55663d 30%,#2e3b22)" role="img" aria-label="Video still of rows of vineyard on rolling hills">
  <div class="play"><svg width="14" height="16" viewBox="0 0 14 16"><path d="M0 0l14 8-14 8z" fill="#fff"/></svg></div>
</div>
<div class="thumb" style="left:620px;background:linear-gradient(135deg,#3a2f25,#b88a4c 55%,#6e5636)" role="img" aria-label="Video still of a plate of noodles">
  <div class="play"><svg width="14" height="16" viewBox="0 0 14 16"><path d="M0 0l14 8-14 8z" fill="#fff"/></svg></div>
</div>
<div class="vcap" style="top:4523px;left:258px">
  <h4>Where to place Plume Vert Harvest on the self</h4>
  <p class="para">Lorem Ipsum is simply dummy text of the printing and typesetting industry.</p>
</div>
<div class="vcap" style="top:4523px;left:620px">
  <h4>Here is a 3600 view of our products</h4>
  <p class="para">Lorem Ipsum is simply dummy text of the printing and typesetting industry.</p>
</div>

<!-- Footer -->
<footer class="abs footer">
  <h5 style="left:80px">PLUME VERT HARVEST</h5>
  <p class="ftext" style="left:80px;top:94px;width:330px">Lorem Ipsum is simply dummy text of the printing and typesetting industry. Lorem Ipsum has been the industry's standard dummy text ever since the 1500s, when an unknown printer took.Lorem Ipsum is simply dummy text</p>

  <h5 style="left:441px">CONTACT US</h5>
  <svg class="abs" style="left:441px;top:100px" width="16" height="22" viewBox="0 0 16 22"><path d="M8 0a8 8 0 0 0-8 8c0 6 8 14 8 14s8-8 8-14a8 8 0 0 0-8-8zm0 11a3 3 0 1 1 0-6 3 3 0 0 1 0 6z" fill="#fff"/></svg>
  <p class="ftext" style="left:475px;top:94px;width:290px">Lorem Ipsum is simply dummy text of the printing and typesetting industry.</p>
  <svg class="abs" style="left:441px;top:170px" width="18" height="18" viewBox="0 0 18 18"><path d="M3 1l4 4-2 2.5c1.3 2.6 3 4.3 5.5 5.5L13 11l4 4-2.5 2.5C8 17 1 10 .5 3.5z" fill="#fff"/></svg>
  <p class="ftext" style="left:475px;top:165px">123 456 7890</p>
  <svg class="abs" style="left:441px;top:220px" width="20" height="14" viewBox="0 0 20 14"><rect width="20" height="14" rx="1" fill="#fff"/><path d="M1 1l9 7 9-7" fill="none" stroke="#1d5e3a" stroke-width="1.5"/></svg>
  <p class="ftext" style="left:475px;top:213px">info@plumevert.com</p>

  <h5 style="left:803px">USEFUL LINKS</h5>
  <div class="links">
    <a href="#" style="top:100px">Home</a>
    <a href="#" style="top:134px">Products</a>
    <a href="#" style="top:168px">Videos</a>
    <a href="#" style="top:202px">About Us</a>
    <a href="#" style="top:236px">How To Order</a>
    <a href="#" style="top:270px">Contact</a>
  </div>
</footer>
<span class="fsocial" style="left:77px"></span>
<span class="fsocial" style="left:127px"></span>
<span class="fsocial" style="left:177px"></span>
<span class="fsocial" style="left:227px"></span>
<div class="copyright">© Plume Vert Harvest - 2019 All Rights Reserved.</div>

</body>
</html>
```